Business Card Design Project

We consult with hotels on setting rates and maximizing a revenue strategy

Industry/Entity Type

Business

Contact Information for Business Card

I am not sure what I want. Our company offers high level consulting to hotels around the country but we are also laid back. I would like something that is professional but also shows the laid back side

```html
<!DOCTYPE html>
<html lang="en">
<head>
<meta charset="utf-8">
<title>Lakemere – Business Card</title>
<link href="https://fonts.googleapis.com/css2?family=Arimo:wght@400;700&display=swap" rel="stylesheet">
<style>
  :root {
    --teal: #1f7a70;
    --teal-deep: #17564f;
    --teal-light: #2e8c80;
    --ink: #2b211d;
    --grey-text: #4a4a4a;
    --rule: #c9c9c9;
    --card-white: #ffffff;
    --page: #e9e7e3;
  }
  * { margin: 0; padding: 0; box-sizing: border-box; }
  html, body {
    width: 1200px; height: 950px; overflow: hidden;
    background: var(--page);
    font-family: "Arimo", Arial, sans-serif;
  }
  .stage {
    position: relative; width: 1200px; height: 950px;
    display: flex; flex-direction: column; align-items: center; justify-content: center; gap: 50px;
  }
  .card {
    position: relative; width: 700px; height: 400px;
    box-shadow: 0 6px 20px rgba(0,0,0,0.18);
  }

  /* Back side */
  .card-back {
    background: linear-gradient(120deg, var(--teal-deep) 0%, var(--teal) 55%, var(--teal-light) 100%);
    color: #fff;
  }
  .card-back .back-mark {
    position: absolute; left: 0; right: 0; top: 150px;
    text-align: center; font-size: 40px; font-weight: 700; letter-spacing: 4px;
    color: #e8f0ef;
  }
  .card-back .back-web {
    position: absolute; left: 0; right: 0; bottom: 48px;
    text-align: center; font-size: 20px; letter-spacing: 1px; color: #d8e6e4;
  }

  /* Front side */
  .card-front {
    background: linear-gradient(160deg, var(--card-white) 60%, #efefef 100%);
  }
  .brand {
    position: absolute; left: 40px; top: 170px;
    display: flex; align-items: center; gap: 14px;
  }
  .brand-square { width: 34px; height: 34px; background: var(--teal); }
  .brand-name {
    font-size: 40px; font-weight: 700; letter-spacing: 2px; color: var(--ink);
  }
  .brand-tagline {
    position: absolute; left: 88px; top: 222px;
    font-size: 14px; font-weight: 700; color: var(--ink);
  }
  .divider {
    position: absolute; left: 370px; top: 100px; width: 1px; height: 200px;
    background: var(--rule);
  }
  .contact { position: absolute; left: 400px; top: 112px; }
  .contact-name { font-size: 25px; font-weight: 700; color: var(--teal); }
  .contact-title { font-size: 19px; color: var(--grey-text); margin-top: 4px; margin-bottom: 10px; }
  .contact-line {
    display: flex; align-items: center; gap: 10px;
    font-size: 18px; color: var(--grey-text); line-height: 27px;
  }
  .contact-line svg { width: 16px; height: 16px; fill: var(--grey-text); flex: none; }
  .contact-line.no-icon { padding-left: 26px; }
</style>
</head>
<body>
<main class="stage">
  <section class="card card-back" aria-label="Card back">
    <div class="back-mark">LAKEMERE</div>
    <div class="back-web">www.LakemereRMS.com</div>
  </section>

  <section class="card card-front" aria-label="Card front">
    <div class="brand">
      <span class="brand-square"></span>
      <span class="brand-name">LAKEMERE</span>
    </div>
    <div class="brand-tagline">Revenue Management Solutions</div>

    <div class="divider"></div>

    <div class="contact">
      <div class="contact-name">Dana Whitmore</div>
      <div class="contact-title">Regional Revenue Manager</div>
      <div class="contact-line">
        <svg viewBox="0 0 16 16" aria-hidden="true"><path d="M3 1h3l1.5 4-2 1.3a9 9 0 0 0 4.2 4.2L11 8.5l4 1.5v3a2 2 0 0 1-2 2A12 12 0 0 1 1 3a2 2 0 0 1 2-2z"/></svg>
        <span>555-014-2290</span>
      </div>
      <div class="contact-line">
        <svg viewBox="0 0 16 16" aria-hidden="true"><rect x="4" y="1" width="8" height="4"/><rect x="1" y="6" width="14" height="6" rx="1"/><rect x="4" y="10" width="8" height="5"/></svg>
        <span>555-017-3364</span>
      </div>
      <div class="contact-line">
        <svg viewBox="0 0 16 16" aria-hidden="true"><path d="M1 3h14v10H1z M1 3l7 6 7-6" fill="none" stroke="#4a4a4a" stroke-width="1.6"/></svg>
        <span>Dana@LakemereRMS.com</span>
      </div>
      <div class="contact-line">
        <svg viewBox="0 0 16 16" aria-hidden="true"><circle cx="8" cy="8" r="7"/></svg>
        <span>www.LakemereRMS.com</span>
      </div>
    </div>
  </section>
</main>
</body>
</html>
```